Kindle Thread Pty Ltd Brochure and New Image Design

Initally we will be needing a A4 Folder design created as well as a Template for a Double Sided Flyer. We need a cutting edge design which we can incorporate into a Brochure, Flyer Handout, Website etc. Basically we are re-branding our company starting with an "About Us" Folder which we will be distributing to potential customers.
We are an Embroidery company that caters for mid-large companies dealing with clothing ranging from Corporate Attire to Workwear. Our current website has more information on what we do and you can use that as a valid reference point (www.kindlethread.com.au), However the website will be step 2 in freshening up our image.
Our company has been thriving over the 20 years we have been in business by supplying a higher quality product as well as Service that is second to none, unfortunately our branding image has been overlooked while we have spent more time/effort on our customer service.
We have used the colours Maroon (PMS 216C) Silver Grey (PMS Cool Gray 7) White and Black. We would like to maintain these colours but incorporate them together in a way that has a more "modern edgey" look.
Target Market(s)
Purchasing / Marketing Officers of Mid-Large Corporate Companies.
Industry/Entity Type
Clothing
Look and feel

```html
<!DOCTYPE html>
<html lang="en">
<head>
<meta charset="utf-8">
<title>Kindle Thread Pty Ltd – Presentation Folder</title>
<link href="https://fonts.googleapis.com/css2?family=Arimo:wght@400;700&display=swap" rel="stylesheet">
<style>
  :root {
    --plum: #7f1d76;
    --paper: #ffffff;
    --ink-light: #ffffff;
    --score: rgba(255,255,255,0.85);
    --photo-wall: #d9d6d2;
    --photo-wood: #c9a98a;
  }
  html, body {
    margin: 0;
    padding: 0;
    width: 1200px;
    height: 910px;
    overflow: hidden;
    background: var(--paper);
  }
  .folder {
    position: relative;
    width: 1200px;
    height: 910px;
    overflow: hidden;
  }
  .folder-dieline {
    position: absolute;
    inset: 0;
  }
  .brand-mark {
    position: absolute;
    display: flex;
    align-items: center;
    gap: 6px;
    font-family: "Arimo", Arial, sans-serif;
    font-weight: 700;
    color: var(--ink-light);
    white-space: nowrap;
  }
  .brand-mark .mark-square {
    width: 10px;
    height: 10px;
    background: var(--ink-light);
  }
  .brand-mark--back {
    left: 163px;
    top: 596px;
    font-size: 15px;
  }
  .brand-mark--front {
    left: 1066px;
    top: 656px;
    font-size: 15px;
  }
  .contact-block {
    position: absolute;
    left: 163px;
    top: 641px;
    margin: 0;
    font-family: "Arimo", Arial, sans-serif;
    font-size: 8.6px;
    line-height: 10.3px;
    color: var(--ink-light);
    font-style: normal;
  }
</style>
</head>
<body>
<main class="folder">
  <svg class="folder-dieline" width="1200" height="910" viewBox="0 0 1200 910">
    <defs>
      <linearGradient id="photoTone" x1="0" y1="0" x2="1" y2="0">
        <stop offset="0" stop-color="#d9d6d2"/>
        <stop offset="0.6" stop-color="#b9b3ad"/>
        <stop offset="1" stop-color="#c9a98a"/>
      </linearGradient>
    </defs>

    <!-- glue flap, left -->
    <polygon class="flap flap--side" fill="var(--plum)"
      points="121,258 103,274 0,562 10,682 121,737"/>
    <line x1="27" y1="594" x2="87" y2="682" stroke="var(--score)" stroke-width="0.8"/>

    <!-- pocket flap, bottom -->
    <path class="flap flap--pocket" fill="var(--plum)"
      d="M121,737 H660 L626,906 H236 L207,868 Q198,862 186,866 L134,818 Q126,808 134,800 L141,793 Q150,786 160,791 Z"/>
    <g class="pocket-scores" stroke="var(--score)" stroke-width="0.8">
      <line x1="293" y1="790" x2="312" y2="771"/>
      <line x1="493" y1="771" x2="512" y2="790"/>
      <line x1="293" y1="874" x2="312" y2="892"/>
      <line x1="493" y1="892" x2="512" y2="874"/>
    </g>

    <!-- back cover -->
    <rect class="panel panel--back" x="121" y="0" width="539" height="737" fill="var(--plum)"/>
    <g class="stitch-lines" stroke="var(--score)" stroke-width="0.8" stroke-dasharray="1.5 1.5">
      <line x1="421" y1="0" x2="421" y2="80"/>
      <line x1="439" y1="0" x2="439" y2="234"/>
      <line x1="458" y1="0" x2="458" y2="312"/>
      <line x1="473" y1="0" x2="473" y2="462"/>
      <line x1="482" y1="0" x2="482" y2="382"/>
      <line x1="491" y1="0" x2="491" y2="165"/>
      <line x1="508" y1="0" x2="508" y2="276"/>
      <line x1="527" y1="0" x2="527" y2="171"/>
      <line x1="545" y1="0" x2="545" y2="382"/>
    </g>

    <!-- front cover -->
    <rect class="panel panel--front" x="660" y="0" width="540" height="737" fill="var(--plum)"/>
    <path class="cover-photo" role="img"
      aria-label="Photo of a model in a black sleeveless corporate dress holding a clutch, in an office with timber panelling"
      fill="url(#photoTone)"
      d="M660,0 H1200 V591 Q900,588 660,460 Z"/>
    <g class="stitch-lines" stroke="var(--score)" stroke-width="0.8" stroke-dasharray="1.5 1.5">
      <line x1="885" y1="641" x2="1035" y2="641"/>
      <line x1="835" y1="652" x2="1035" y2="652"/>
      <line x1="738" y1="662" x2="1035" y2="662"/>
      <line x1="790" y1="668" x2="1035" y2="668"/>
      <line x1="959" y1="674" x2="1035" y2="674"/>
      <line x1="857" y1="684" x2="1035" y2="684"/>
      <line x1="926" y1="696" x2="1035" y2="696"/>
    </g>
  </svg>

  <div class="brand-mark brand-mark--back"><span class="mark-square"></span>Kindle Thread</div>

  <address class="contact-block">
    Kindle Thread Embroidery P/L<br>
    22 Harbour Loom St<br>
    Riverton NSW 2190 AUSTRALIA<br>
    Phone: +612 9000 1234<br>
    Facsimile: +612 9000 5678<br>
    enquiries@kindlethread.com.au
  </address>

  <div class="brand-mark brand-mark--front"><span class="mark-square"></span>Kindle Thread</div>
</main>
</body>
</html>
```